Market online tutoring + Back to School + give Support for students school work K to 12 Grade

To promote my tutoring business online need to create a two sided flyer. Need to get the attention of parents and educators who looking for help to support the digital learning of their students due to COVID-19 lock down. I need to project and differentiate that we offer support for online school with individualized learning . We tutor Elementary to High school students on all subjects you may take a look at my website qnacademyga.com for additional info and also I can provide
Updates

Hi All Due to Covid, we were unable to work on this project on time as originally planned. We were given an extension until March 15 and we will complete it by then. Sorry for any inconvenience and Thank you for your support. -QN Academy

Target Market(s)

Parents and students

Industry/Entity Type

Education

Requirements
Must have
• For online less fine print on the first page. The phone number and support text message. Back to School , Support Online learning KEV/NUR test prep should have some focus
Nice to have
• Discuss the platform We created a platform with live instructor interaction, virtual classroom, instructional videos, assessments, and practice to support every individual student’s need. We are confident in our ability to provide the most effective distance learning experience.
Should not have
• too much clunky and packed with content. Should be easy to read with color

```html
<!DOCTYPE html>
<html lang="en">
<head>
<meta charset="utf-8">
<title>QN Academy – Back to School Flyer</title>
<link href="https://fonts.googleapis.com/css2?family=Montserrat:ital,wght@0,500;0,600;0,700;0,800;1,600;1,700&display=swap" rel="stylesheet">
<style>
  :root{
    --stage:#9d9d9d;
    --red:#9c1a2b;
    --red-deep:#74101d;
    --teal:#1bb3a0;
    --navy:#0f4656;
    --yellow:#ffe21a;
    --panel:#f0f0f0;
    --ink:#2a2a2a;
    --white:#ffffff;
  }
  *{box-sizing:border-box;margin:0;padding:0}
  html,body{width:1200px;height:1200px;overflow:hidden}
  body{background:var(--stage);font-family:"Montserrat",Arial,sans-serif;position:relative}
  ul,ol{list-style:none}

  .flyer{position:absolute;top:260px;width:550px;height:680px;background:var(--white);overflow:hidden;box-shadow:0 10px 24px rgba(0,0,0,.35)}
  .flyer--front{left:35px}
  .flyer--back{left:615px}
  .shapes{position:absolute;inset:0;width:550px;height:680px}

  .photo{position:absolute;left:0;top:0;width:550px}
  .photo--study{height:300px;background:linear-gradient(135deg,#e7e2da 0%,#c9d7e3 45%,#7f9fb8 100%)}
  .photo--chalk{height:330px;background:radial-gradient(circle at 55% 55%,#4a5064 0%,#2d3243 55%,#1f2331 100%)}

  /* front */
  .headline{position:absolute;top:300px;left:0;width:550px;text-align:center;color:var(--white)}
  .headline__title{font-size:37px;font-weight:800;letter-spacing:-.5px}
  .headline__sub{font-size:20px;font-weight:700;font-style:italic;margin-top:2px}
  .support-pill{position:absolute;top:442px;left:58px;width:430px;height:50px;border-radius:25px;background:var(--navy);color:var(--white);text-align:center;padding-top:5px}
  .support-pill__lead{font-size:19px;font-weight:600;line-height:22px}
  .support-pill__detail{font-size:13px;font-weight:600;font-style:italic;line-height:16px}

  .features{position:absolute;top:505px;left:0;width:550px;height:105px;background:var(--panel);display:flex}
  .feature{flex:1;display:flex;flex-direction:column;align-items:center;padding-top:10px;border-left:1px solid #dcdcdc}
  .feature:first-child{border-left:none}
  .feature__icon{width:52px;height:52px;border-radius:50%;background:radial-gradient(circle at 35% 30%,#c22a3c,var(--red-deep));border:3px solid #f7f7f7;box-shadow:0 2px 4px rgba(0,0,0,.3);display:flex;align-items:center;justify-content:center}
  .feature__label{margin-top:8px;font-size:11px;font-weight:600;font-style:italic;color:var(--ink);text-align:center;line-height:12px}

  /* back */
  .services-tab{position:absolute;top:322px;left:120px;width:310px;height:80px;background:linear-gradient(var(--red),var(--red-deep));border-radius:0 0 16px 16px;color:var(--white);font-size:36px;font-weight:800;text-align:center;line-height:86px;letter-spacing:.5px}
  .services{position:absolute;top:420px;left:12px;width:526px;display:grid;grid-template-columns:repeat(4,1fr);grid-template-rows:repeat(2,84px);gap:10px 6px}
  .service{background:var(--white);box-shadow:0 2px 5px rgba(0,0,0,.25);display:flex;flex-direction:column;align-items:center;padding-top:6px}
  .service__num{width:36px;height:36px;border-radius:50%;background:var(--white);box-shadow:0 2px 4px rgba(0,0,0,.25);color:var(--teal);font-size:21px;font-weight:800;display:flex;align-items:center;justify-content:center}
  .service__name{flex:1;display:flex;align-items:center;text-align:center;font-size:10px;font-weight:700;color:var(--ink);text-transform:uppercase;line-height:12px;padding:0 6px}

  /* shared footer */
  .footer{position:absolute;left:0;bottom:0;width:550px;height:70px;display:flex}
  .footer__contact{width:365px;background:var(--navy);color:var(--white);padding:8px 0 0 16px;position:relative}
  .footer__phone{display:flex;align-items:center;gap:12px;color:var(--yellow);font-size:27px;font-weight:800;line-height:32px}
  .footer__details{display:flex;gap:14px;margin-top:5px;font-size:7.5px;font-weight:600;font-style:italic;line-height:9px}
  .footer__item{display:flex;align-items:flex-start;gap:6px}
  .footer__brand{flex:1;background:var(--white);display:flex;align-items:center;justify-content:center;gap:8px}
  .brand__mark{width:14px;height:14px;background:var(--navy)}
  .brand__name{font-size:20px;font-weight:700;color:var(--navy)}
  .ico{flex:none}
</style>
</head>
<body>

<!-- Front side -->
<section class="flyer flyer--front">
  <div class="photo photo--study" role="img" aria-label="Photo of a young student with headphones attending an online class with a teacher on a desktop screen"></div>
  <svg class="shapes" viewBox="0 0 550 680" aria-hidden="true">
    <defs>
      <linearGradient id="redBand" x1="0" y1="0" x2="0" y2="1">
        <stop offset="0" stop-color="#8c1524"/><stop offset="1" stop-color="#a81d30"/>
      </linearGradient>
    </defs>
    <rect x="22" y="22" width="506" height="250" fill="none" stroke="#fff" stroke-width="1.5"/>
    <path d="M0 175 Q180 300 550 200 L550 290 L0 290 Z" fill="var(--teal)"/>
    <path d="M0 195 Q200 320 550 215 L550 430 Q300 400 0 455 Z" fill="url(#redBand)"/>
    <path d="M0 455 Q300 400 550 430 L550 505 L0 505 Z" fill="#fff"/>
    <path d="M380 412 Q480 420 550 450 L550 432 Q470 415 380 412 Z" fill="var(--teal)"/>
  </svg>

  <header class="headline">
    <h1 class="headline__title">BACK TO SCHOOL</h1>
    <p class="headline__sub">Support Online learning KEV/NUR test prep</p>
  </header>

  <div class="support-pill">
    <p class="support-pill__lead">we offer support for</p>
    <p class="support-pill__detail">online school with individualized learning</p>
  </div>

  <ul class="features">
    <li class="feature">
      <span class="feature__icon"><svg width="26" height="26" viewBox="0 0 28 28" fill="none" stroke="#fff" stroke-width="1.8"><rect x="6" y="3" width="19" height="13"/><circle cx="6" cy="19" r="2.5"/><path d="M2 26v-2a4 4 0 0 1 8 0v2M9 12l5-4 4 3 4-5"/></svg></span>
      <span class="feature__label">instructor interaction</span>
    </li>
    <li class="feature">
      <span class="feature__icon"><svg width="26" height="26" viewBox="0 0 28 28" fill="none" stroke="#fff" stroke-width="1.8"><rect x="5" y="6" width="18" height="12"/><path d="M2 22h24M11 12l3-2 3 2-3 2z"/></svg></span>
      <span class="feature__label">virtual classroom</span>
    </li>
    <li class="feature">
      <span class="feature__icon"><svg width="26" height="26" viewBox="0 0 28 28" fill="#fff"><path d="M14 4c6 0 10 3.8 10 8.5S20 21 14 21c-1 0-2-.1-3-.4L6 24l1.2-4.6C5.2 17.8 4 15.3 4 12.5 4 7.8 8 4 14 4z"/><rect x="9" y="11" width="10" height="3" fill="#9c1a2b"/></svg></span>
      <span class="feature__label">instructional videos</span>
    </li>
    <li class="feature">
      <span class="feature__icon"><svg width="26" height="26" viewBox="0 0 28 28" fill="none" stroke="#fff" stroke-width="1.8"><path d="M6 3h12l4 4v18H6z"/><path d="M9 9h8M9 13h6"/><circle cx="16" cy="19" r="3.5"/><path d="M18.5 21.5L22 25"/></svg></span>
      <span class="feature__label">assessments, and<br>practice</span>
    </li>
  </ul>

  <footer class="footer">
    <div class="footer__contact">
      <p class="footer__phone"><svg class="ico" width="12" height="12" viewBox="0 0 24 24" fill="#fff"><path d="M6.6 10.8a15 15 0 0 0 6.6 6.6l2.2-2.2a1 1 0 0 1 1-.25 11.4 11.4 0 0 0 3.6.6 1 1 0 0 1 1 1V20a1 1 0 0 1-1 1A17 17 0 0 1 3 4a1 1 0 0 1 1-1h3.5a1 1 0 0 1 1 1c0 1.25.2 2.45.6 3.6a1 1 0 0 1-.25 1z"/></svg>404-555-0187</p>
      <div class="footer__details">
        <p class="footer__item"><svg class="ico" width="10" height="10" viewBox="0 0 24 24" fill="#fff"><circle cx="12" cy="12" r="11"/></svg>2450 Maple Ridge Pkwy, Suite 210<br>Duluth, GA 30096</p>
        <p class="footer__item"><svg class="ico" width="10" height="10" viewBox="0 0 24 24" fill="#fff"><circle cx="12" cy="12" r="11"/></svg>customerservice@qnacademyga.com</p>
      </div>
    </div>
    <div class="footer__brand"><span class="brand__mark"></span><span class="brand__name">QN Academy</span></div>
  </footer>
</section>

<!-- Back side -->
<section class="flyer flyer--back">
  <div class="photo photo--chalk" role="img" aria-label="Photo of a little girl in glasses reading a large book in front of a chalkboard covered in equations"></div>
  <svg class="shapes" viewBox="0 0 550 680" aria-hidden="true">
    <rect x="22" y="22" width="506" height="270" fill="none" stroke="#fff" stroke-width="1.5"/>
    <path d="M0 270 Q260 360 550 255 L550 290 Q260 380 0 300 Z" fill="var(--teal)"/>
    <path d="M0 300 Q260 380 550 290 L550 680 L0 680 Z" fill="var(--panel)"/>
  </svg>

  <h2 class="services-tab">OUR SERVICES</h2>

  <ol class="services">
    <li class="service"><span class="service__num">1</span><span class="service__name">Core Mathematics</span></li>
    <li class="service"><span class="service__num">2</span><span class="service__name">Core Reading /<br>Writing</span></li>
    <li class="service"><span class="service__num">3</span><span class="service__name">Critical Thinking</span></li>
    <li class="service"><span class="service__num">4</span><span class="service__name">Computer<br>Programming</span></li>
    <li class="service"><span class="service__num">5</span><span class="service__name">College<br>Preparation</span></li>
    <li class="service"><span class="service__num">6</span><span class="service__name">State<br>Benchmarks</span></li>
    <li class="service"><span class="service__num">7</span><span class="service__name">Kids Programming</span></li>
    <li class="service"><span class="service__num">8</span><span class="service__name">Private Session</span></li>
  </ol>

  <footer class="footer">
    <div class="footer__contact">
      <p class="footer__phone"><svg class="ico" width="12" height="12" viewBox="0 0 24 24" fill="#fff"><path d="M6.6 10.8a15 15 0 0 0 6.6 6.6l2.2-2.2a1 1 0 0 1 1-.25 11.4 11.4 0 0 0 3.6.6 1 1 0 0 1 1 1V20a1 1 0 0 1-1 1A17 17 0 0 1 3 4a1 1 0 0 1 1-1h3.5a1 1 0 0 1 1 1c0 1.25.2 2.45.6 3.6a1 1 0 0 1-.25 1z"/></svg>404-555-0187</p>
      <div class="footer__details">
        <p class="footer__item"><svg class="ico" width="10" height="10" viewBox="0 0 24 24" fill="#fff"><circle cx="12" cy="12" r="11"/></svg>2450 Maple Ridge Pkwy, Suite 210<br>Duluth, GA 30096</p>
        <p class="footer__item"><svg class="ico" width="10" height="10" viewBox="0 0 24 24" fill="#fff"><circle cx="12" cy="12" r="11"/></svg>customerservice@qnacademyga.com</p>
      </div>
    </div>
    <div class="footer__brand"><span class="brand__mark"></span><span class="brand__name">QN Academy</span></div>
  </footer>
</section>

</body>
</html>
```